Solvane Glow LED - E- Commerce site

We need a website designed for an LED Billboard company that sells:
1) LED Billboards (Sales & Rental)
2) LED Gas Station lights
3) Truss Systems (Sales & Rental)
4) Sound Systems (Sales & Rental)

Attached are websites that sell similar products as Solvane Glow LED. Target market is for business, property managers and event coordinators.
This site will need to be an e-commerce site where customers can purchase the product directly from the site. What I'm looking for is a design layout to start.

Conceptual Web Designs:
http://example-panelora.test/index.html
http://www.vormpix.com/
http://www.droneplayaudio.com/
http://www.quillmarkdisplay.com/

Attached is the logo of the company: Please note that the new spelling of the logo is "Solvane Glow LED" using domain " SolvaneGlowLED.com

Industry/Entity Type

Gas Station

Number of Pages Required

5+ page

Requirements
Must have
• 1) E-Commerce - Customers will need to be able to order product from the site.
• 2) Customers will also have the option to rent the product as well.
Nice to have
• I like the image of the attached website, that has a video clip loop
• http://www.quillmarkdisplay.com/

```html
<!DOCTYPE html>
<html lang="en">
<head>
<meta charset="utf-8">
<title>Solvane Glow LED</title>
<link href="https://fonts.googleapis.com/css2?family=Source+Sans+3:wght@400;600;700&display=swap" rel="stylesheet">
<style>
:root{
  --red:#e4262a;
  --yellow:#fcc70c;
  --black:#141414;
  --dark:#1d1d1d;
  --grey-page:#ececec;
  --grey-band:#f0f0f0;
  --grey-news:#5f5f5f;
  --text:#4a4a4a;
  --text-light:#6d6d6d;
  --white:#ffffff;
}
*{box-sizing:border-box;margin:0;padding:0}
html,body{width:1200px;height:2723px;overflow:hidden}
body{background:var(--grey-page);font-family:"Source Sans 3",Arial,sans-serif;color:var(--text);position:relative}
.abs{position:absolute}
a{color:inherit;text-decoration:none}

/* header */
.site-header{left:15px;top:0;width:1170px;height:155px;background:var(--black)}
.utility-bar{left:617px;top:15px;width:537px;height:49px;background:var(--yellow);border-radius:0 0 8px 8px;display:flex;align-items:center;justify-content:center;gap:14px;font-size:15px;font-weight:600;color:var(--white);letter-spacing:.3px}
.utility-bar .sep{width:1px;height:20px;background:rgba(255,255,255,.7)}
.utility-bar svg{vertical-align:middle}
.search{left:879px;top:87px;width:275px;height:38px;border:2px solid #8a8a8a;border-radius:6px;display:flex;align-items:center;padding:0 8px;gap:8px;font-size:11px;font-weight:700;color:var(--white)}
.search .divider{width:1px;height:22px;background:#8a8a8a}
.search .field{flex:1;height:16px;background:var(--white);border-radius:8px;margin-left:6px}
.brand{left:45px;top:42px;display:flex;align-items:center;gap:10px;z-index:3}
.brand .dot{width:120px;height:120px;border-radius:50%;background:var(--black);border:8px solid var(--red)}
.brand-name{left:58px;top:92px;width:110px;text-align:center;font-size:19px;font-weight:700;line-height:1.05;color:var(--yellow);z-index:4}
.main-nav{left:15px;top:155px;width:1170px;height:48px;background:var(--red);display:flex;align-items:center;padding-left:163px;gap:25px;font-size:17px;font-weight:700;color:var(--white);text-transform:uppercase}
.main-nav .active{color:var(--yellow)}

/* hero */
.hero{left:15px;top:203px;width:1170px;height:450px;background:linear-gradient(100deg,#1a3b4a 0%,#402a55 22%,#0d2a7a 40%,#1c56b8 52%,#16284a 64%,#2d6b3a 78%,#6a2050 100%)}
.hero-arrow{top:440px;width:28px;height:28px;border-radius:50%;background:#6fb33a;display:flex;align-items:center;justify-content:center}
.intro{left:15px;top:653px;width:1170px;height:169px;background:var(--red);text-align:center;color:var(--white)}
.intro p{position:absolute;left:60px;top:22px;width:1050px;font-size:21.5px;font-weight:700;line-height:1.25}
.btn-outline,.btn-solid{position:absolute;top:97px;height:49px;border-radius:8px;font-size:21px;font-weight:600;display:flex;align-items:center;justify-content:center;text-transform:uppercase}
.btn-outline{left:245px;width:330px;border:3px solid var(--white);color:var(--white)}
.btn-solid{left:595px;width:328px;background:var(--white);color:var(--dark)}

/* sections */
.featured{left:15px;top:822px;width:1170px;height:590px;background:var(--white)}
.latest{left:15px;top:1412px;width:1170px;height:554px;background:var(--grey-band)}
.support{left:15px;top:1966px;width:1170px;height:352px;background:var(--white)}
.section-title{display:flex;align-items:center;gap:10px;font-size:31px;color:#555;text-transform:uppercase;letter-spacing:.2px}
.section-title .mark{width:38px;height:38px;border-radius:50%;border:5px solid var(--red)}
.shop-link{left:893px;top:908px;font-size:14px;font-weight:600;color:#555;letter-spacing:.3px}

.product{position:absolute;width:260px}
.product .photo{width:260px;height:182px}
.product h3{margin-top:24px;font-size:16px;font-weight:700;color:#555;text-transform:uppercase}
.product p{font-size:16px;color:var(--text-light);line-height:1.5;margin-top:2px}
.product .price{font-size:22px;font-weight:700;color:#333;margin-top:21px}
.btn-cart{display:flex;align-items:center;justify-content:center;width:160px;height:41px;background:var(--yellow);border-radius:5px;color:var(--white);font-size:17px;font-weight:700;text-transform:uppercase;margin-top:17px}

.card{position:absolute;top:1548px;width:255px;height:369px;background:linear-gradient(#f4f4f4,#dcdcdc);border:3px solid var(--white);box-shadow:0 2px 6px rgba(0,0,0,.18);text-align:center}
.card .photo{width:249px;height:182px}
.card h3{margin-top:17px;font-size:16px;font-weight:600;color:#555;text-transform:uppercase}
.card p{font-size:16px;font-weight:600;color:#444;margin-top:2px}
.card .price{font-size:24px;font-weight:700;color:#333;margin-top:1px}
.card .btn-cart{margin:14px auto 0;width:165px;height:41px;box-shadow:0 2px 3px rgba(0,0,0,.2)}

.tone-red{background:linear-gradient(135deg,#2a0a08,#a83614 45%,#3a0e0a)}
.tone-blue{background:linear-gradient(135deg,#0c1b5a,#2d4fbf 50%,#0b1c4a)}
.tone-night{background:linear-gradient(135deg,#1a1f3a,#3a4a8a 45%,#6a4a2a)}
.tone-street{background:linear-gradient(135deg,#7a2a1a,#c8502a 40%,#4a4a55)}

.support-text{left:91px;top:2102px;width:1018px;text-align:center;font-size:16px;line-height:1.5;color:var(--text-light)}
.btn-red{left:519px;top:2225px;width:162px;height:40px;background:var(--red);border-radius:5px;color:var(--white);font-size:18px;font-weight:700;display:flex;align-items:center;justify-content:center;text-transform:uppercase}

/* newsletter */
.newsletter{left:15px;top:2318px;width:1170px;height:91px;background:var(--grey-news)}
.newsletter h2{position:absolute;left:103px;top:25px;font-size:31px;font-weight:600;color:var(--white)}
.input{position:absolute;top:23px;width:229px;height:42px;background:var(--white);font-size:14px;font-weight:600;color:#333;padding:0 18px;display:flex;align-items:center}
.btn-subscribe{position:absolute;left:963px;top:23px;width:106px;height:42px;background:var(--black);color:var(--white);font-size:13px;font-weight:600;display:flex;align-items:center;justify-content:center}

/* footer */
.footer{left:15px;top:2409px;width:1170px;height:246px;background:var(--red);overflow:hidden}
.footer .slab{position:absolute;left:0;top:0;width:1170px;height:246px}
.footer-col{position:absolute;top:30px;color:var(--white)}
.footer-col h4{font-size:16px;font-weight:700;text-transform:uppercase;margin-bottom:12px}
.footer-col li{list-style:none;font-size:13.5px;font-weight:700;line-height:19.4px;text-transform:uppercase}
.social li{display:flex;align-items:center;gap:12px;line-height:40px;font-size:15px}
.social .ico{width:26px;height:26px;border-radius:50%;background:var(--white)}
.footer-brand{left:1025px;top:2532px;transform:translate(-50%,-50%);display:flex;align-items:center;gap:12px}
.footer-brand .dot{width:22px;height:22px;border-radius:50%;background:var(--red)}
.footer-brand span{font-size:24px;font-weight:700;color:var(--yellow);line-height:1.05;width:110px}
.copyright{left:15px;top:2655px;width:1170px;height:52px;text-align:center;font-size:12px;font-weight:600;color:#555;line-height:52px;text-transform:uppercase}
</style>
</head>
<body>

<header class="site-header abs"></header>
<div class="utility-bar abs">
  <span>CALL US</span>
  <svg width="20" height="20" viewBox="0 0 24 24"><circle cx="12" cy="12" r="10.5" fill="none" stroke="#fff" stroke-width="1.6"/><path d="M8.5 7c.6-.6 1.3-.5 1.7.1l1 1.6c.3.5.2 1-.2 1.4l-.7.6c.6 1.3 1.6 2.3 2.9 2.9l.6-.7c.4-.4.9-.5 1.4-.2l1.6 1c.6.4.7 1.1.1 1.7-1 1-2.4 1.2-3.7.5-2.3-1.2-4.1-3-5.3-5.3-.7-1.3-.5-2.7.5-3.6z" fill="#fff"/></svg>
  <span>555-014-2273</span>
  <span class="sep"></span>
  <span>LOGIN</span>
  <span class="sep"></span>
  <span>SIGN UP</span>
  <span class="sep"></span>
  <svg width="22" height="20" viewBox="0 0 24 22"><path d="M1 2h4l3 12h12l3-9H7" fill="none" stroke="#fff" stroke-width="2" stroke-linejoin="round"/><circle cx="10" cy="18.5" r="1.8" fill="#fff"/><circle cx="18" cy="18.5" r="1.8" fill="#fff"/></svg>
  <span>CART</span>
</div>
<div class="search abs">
  <svg width="18" height="18" viewBox="0 0 20 20"><circle cx="8" cy="8" r="6" fill="none" stroke="#fff" stroke-width="2"/><path d="M12.5 12.5l5 5" stroke="#fff" stroke-width="2.4" stroke-linecap="round"/></svg>
  <span class="divider"></span>
  <span>SEARCH SITE</span>
  <span class="field"></span>
</div>
<div class="brand abs"><span class="dot"></span></div>
<div class="brand-name abs">Solvane Glow LED</div>

<nav class="main-nav abs">
  <a class="active">Home</a><a>About Us</a><a>LED Billboards</a><a>LED Gas Station</a><a>Truss System</a><a>Sound System</a><a>Support</a><a>Contact</a>
</nav>

<div class="hero abs" role="img" aria-label="Night street scene with large illuminated LED billboards and neon signs"></div>
<div class="hero-arrow abs" style="left:51px"><svg width="14" height="14" viewBox="0 0 14 14"><path d="M9 2L4 7l5 5" fill="none" stroke="#fff" stroke-width="2.5"/></svg></div>
<div class="hero-arrow abs" style="left:1119px"><svg width="14" height="14" viewBox="0 0 14 14"><path d="M5 2l5 5-5 5" fill="none" stroke="#fff" stroke-width="2.5"/></svg></div>

<section class="intro abs">
  <p>Lorem ipsum dolor sit amet, consectetuer adipiscing elit, sed diam nonummy nibh euismod tinci dunt ut laoreet dolore magna aliquam erat volutpat. Ut wisi enim ad minim veniam, consequat.</p>
  <a class="btn-outline">Learn more about us</a>
  <a class="btn-solid">Browse our products</a>
</section>

<section class="featured abs"></section>
<h2 class="section-title abs" style="left:65px;top:885px"><span class="mark"></span>Featured Products</h2>
<a class="shop-link abs">SHOP MOST POPULAR PRODUCTS &nbsp;›</a>

<div class="product" style="left:65px;top:967px">
  <div class="photo tone-red" role="img" aria-label="Departure board with orange LED text"></div>
  <h3>Product #1</h3><p>Lorem ipsum dolor sit amet, con sectetuer adipiscing elit</p>
  <div class="price">$1200.00</div><a class="btn-cart">Add to cart</a>
</div>
<div class="product" style="left:336px;top:967px">
  <div class="photo tone-blue" role="img" aria-label="Blue LED flight information display"></div>
  <h3>Product #2</h3><p>Lorem ipsum dolor sit amet, con sectetuer adipiscing elit</p>
  <div class="price">$1200.00</div><a class="btn-cart">Add to cart</a>
</div>
<div class="product" style="left:606px;top:967px">
  <div class="photo tone-night" role="img" aria-label="Building facade with large video screens at night"></div>
  <h3>Product #3</h3><p>Lorem ipsum dolor sit amet, con sectetuer adipiscing elit</p>
  <div class="price">$1200.00</div><a class="btn-cart">Add to cart</a>
</div>
<div class="product" style="left:877px;top:967px">
  <div class="photo tone-street" role="img" aria-label="Theatre marquee sign above a busy city street"></div>
  <h3>Product #4</h3><p>Lorem ipsum dolor sit amet, con sectetuer adipiscing elit</p>
  <div class="price">$1200.00</div><a class="btn-cart">Add to cart</a>
</div>

<section class="latest abs"></section>
<h2 class="section-title abs" style="left:458px;top:1468px"><span class="mark"></span>Latest Products</h2>

<div class="card" style="left:74px">
  <div class="photo tone-red" role="img" aria-label="Departure board with orange LED text"></div>
  <h3>Product #1</h3><p>Lorem ipsum dolor sit amet</p><div class="price">$1224.00</div><a class="btn-cart">Add to cart</a>
</div>
<div class="card" style="left:341px">
  <div class="photo tone-blue" role="img" aria-label="Blue LED flight information display"></div>
  <h3>Product #2</h3><p>Lorem ipsum dolor sit amet</p><div class="price">$1224.00</div><a class="btn-cart">Add to cart</a>
</div>
<div class="card" style="left:608px">
  <div class="photo tone-night" role="img" aria-label="Building facade with large video screens at night"></div>
  <h3>Product #3</h3><p>Lorem ipsum dolor sit amet</p><div class="price">$1224.00</div><a class="btn-cart">Add to cart</a>
</div>
<div class="card" style="left:873px">
  <div class="photo tone-street" role="img" aria-label="Theatre marquee sign above a busy city street"></div>
  <h3>Product #4</h3><p>Lorem ipsum dolor sit amet</p><div class="price">$1224.00</div><a class="btn-cart">Add to cart</a>
</div>

<section class="support abs"></section>
<h2 class="section-title abs" style="left:522px;top:2022px"><span class="mark"></span>Support</h2>
<p class="support-text abs">Lorem ipsum dolor sit amet, consectetuer adipiscing elit, sed diam nonummy nibh euismod tincidunt ut laoreet dolore magna aliquam erat volutpat. Ut wisi enim ad minim veniam, quis nostrud exerci tation ullamcorper suscipit lobortis nisl ut aliquip ex ea commodo consequat. Duis autem vel eum iriure dolor in hendrerit in vulputate velit esse molestie consequat, vel illum dolore eu feugiat nulla facilisis at vero eros et accumsan et iusto odio dignissim qui blandit praesent luptatum zzril delenit augue duis dolore te feugait nulla facilisi</p>
<a class="btn-red abs">Learn more</a>

<section class="newsletter abs">
  <h2>Subscribe to Newsletter</h2>
  <div class="input" style="left:484px">Name</div>
  <div class="input" style="left:724px">Email</div>
  <a class="btn-subscribe">SUBSCRIBE</a>
</section>

<footer class="footer abs">
  <svg class="slab" viewBox="0 0 1170 246" preserveAspectRatio="none"><polygon points="938,0 1170,0 1170,246 796,246" fill="#141414"/></svg>
  <div class="footer-col" style="left:58px"><h4>Menu</h4><ul><li>About Us</li><li>LED Billboards</li><li>LED Gas Station</li><li>Trust System</li><li>Sound System</li><li>Support</li><li>Contact</li></ul></div>
  <div class="footer-col" style="left:239px"><h4>Information</h4><ul><li>FAQ</li><li>Orders</li><li>Delivery Information</li><li>Privacy Policy</li><li>Returns Policy</li><li>Terms of Use</li></ul></div>
  <div class="footer-col" style="left:470px"><h4>My Account</h4><ul><li>Account</li><li>My Cart</li><li>Order History</li><li>Wish List</li><li>Newsletter</li></ul></div>
  <div class="footer-col social" style="left:642px"><h4 style="margin-bottom:2px">Follow Us</h4><ul><li><span class="ico"></span>Friendwall</li><li><span class="ico"></span>Chirpline</li><li><span class="ico"></span>Snapframe</li><li><span class="ico"></span>Circlenet</li></ul></div>
</footer>
<div class="footer-brand abs"><span class="dot"></span><span>Solvane Glow LED</span></div>

<div class="copyright abs">© 2016 Solvane Glow LED. All rights reserved.</div>

</body>
</html>
```